Need a business card for our overland brand!

We had the logo made and we need a great design for our business card. Use the logo provide or tweak it however you see fit.

Contact Information for Business Card

Name, Title, Telephone, email, website

```html
<!DOCTYPE html>
<html lang="en">
<head>
<meta charset="utf-8">
<title>Summit Traverse — Business Card</title>
<link rel="stylesheet" href="https://fonts.googleapis.com/css2?family=Oswald:wght@300;400;600;700&display=swap">
<style>
  :root {
    --slate: #344a60;
    --slate-deep: #2c3f53;
    --ice: #2ea6c9;
    --paper: #ffffff;
    --stage: #e8e5e0;
    --text-light: #eef3f7;
  }
  * { box-sizing: border-box; margin: 0; padding: 0; }
  html, body { width: 1200px; height: 780px; overflow: hidden; }
  body {
    background: var(--stage);
    font-family: "Oswald", sans-serif;
    position: relative;
  }
  .card {
    position: absolute;
    top: 128px;
    width: 300px;
    height: 525px;
    overflow: hidden;
    box-shadow: 0 10px 28px rgba(0,0,0,0.18);
  }
  .card--front { left: 230px; background: var(--slate); }
  .card--back  { left: 670px; background: var(--slate); }

  .front__header {
    position: absolute; left: 0; top: 0;
    width: 300px; height: 232px;
    background: var(--paper);
  }
  .brand-name {
    position: absolute; left: 0; right: 0;
    text-align: center;
    font-weight: 700;
    text-transform: uppercase;
    line-height: 0.92;
    letter-spacing: 1px;
  }
  .front__header .brand-name {
    top: 70px;
    font-size: 46px;
    color: var(--slate-deep);
  }
  .front__ridge {
    position: absolute; left: 0; top: 212px;
    width: 300px; height: 80px;
    display: block;
  }

  .contact-block {
    position: absolute; left: 56px; top: 318px;
    width: 220px;
  }
  .contact-block__name {
    font-size: 31px; font-weight: 600;
    color: var(--ice);
    text-transform: uppercase;
    letter-spacing: 1px;
    line-height: 1.05;
  }
  .contact-block__title {
    font-size: 14px; font-weight: 400;
    color: var(--text-light);
    text-transform: uppercase;
    letter-spacing: 1px;
    margin-top: 4px;
  }
  .contact-block__rule {
    width: 52px; height: 2px;
    background: var(--ice);
    margin: 22px 0 18px;
  }
  .contact-list { list-style: none; }
  .contact-list__item {
    display: flex; align-items: center; gap: 12px;
    font-size: 12.5px; font-weight: 300;
    color: var(--text-light);
    text-transform: uppercase;
    letter-spacing: 0.8px;
    margin-bottom: 10px;
  }
  .contact-list__icon {
    width: 20px; height: 20px;
    border-radius: 4px;
    background: var(--ice);
    flex: none;
  }

  .card--back .brand-name {
    top: 214px;
    font-size: 54px;
    color: var(--ice);
  }
</style>
</head>
<body>

  <section class="card card--front" aria-label="Business card front">
    <div class="front__header">
      <div class="brand-name">Summit<br>Traverse</div>
    </div>

    <svg class="front__ridge" viewBox="0 0 300 80" role="img" aria-label="Mountain ridge illustration in ice blue over slate">
      <defs>
        <linearGradient id="ridgeTone" x1="0" y1="0" x2="0" y2="1">
          <stop offset="0" stop-color="#ffffff"/>
          <stop offset="0.35" stop-color="#2ea6c9"/>
          <stop offset="1" stop-color="#344a60"/>
        </linearGradient>
      </defs>
      <rect width="300" height="80" fill="url(#ridgeTone)"/>
    </svg>

    <div class="contact-block">
      <h1 class="contact-block__name">Daniel Hart</h1>
      <p class="contact-block__title">Founder &amp; CEO</p>
      <div class="contact-block__rule"></div>
      <ul class="contact-list">
        <li class="contact-list__item">
          <svg class="contact-list__icon" viewBox="0 0 20 20" aria-hidden="true">
            <path d="M7 5.5l1.6 2.4-1.1 1.1c.7 1.4 1.9 2.6 3.3 3.3l1.1-1.1 2.4 1.6-.9 1.8c-3.8-.4-7.3-3.9-7.7-7.7z" fill="#fff"/>
          </svg>
          (555) 014-2288
        </li>
        <li class="contact-list__item">
          <svg class="contact-list__icon" viewBox="0 0 20 20" aria-hidden="true">
            <rect x="5" y="6.5" width="10" height="7" fill="none" stroke="#fff" stroke-width="1.3"/>
            <path d="M5 6.5l5 4 5-4" fill="none" stroke="#fff" stroke-width="1.3"/>
          </svg>
          info@summittraverse.com
        </li>
        <li class="contact-list__item">
          <svg class="contact-list__icon" viewBox="0 0 20 20" aria-hidden="true">
            <circle cx="10" cy="10" r="4.8" fill="none" stroke="#fff" stroke-width="1.2"/>
            <ellipse cx="10" cy="10" rx="2" ry="4.8" fill="none" stroke="#fff" stroke-width="1"/>
            <path d="M5.2 10h9.6" stroke="#fff" stroke-width="1"/>
          </svg>
          summittraverse.com
        </li>
      </ul>
    </div>
  </section>

  <section class="card card--back" aria-label="Business card back">
    <div class="brand-name">Summit<br>Traverse</div>
  </section>

</body>
</html>
```